SEO wiki for a know-how website (rankvale.ch)

Hi,

i need a know-how wiki for an SEO website that looks similar to:

http://demo.plinkora.com/#knowhow

With following know-how categories instead of "account settings" and "API questions":
- Content SEO
- Technical SEO
- Link building
- Influencer marketing
- paid marketing
- analytics & measurement

So i Need the following pages:
1. Landing page with the categories, the search bar and the side-bar
- Sidebar has latest articles, popular articles and categories (in this order)
- On top a nice logo
- on top right -> blog, contact
- on top right below -> social media buttons: brivella, chirpnet

2. a blog site with
- headline
- sub-headline
- date, name
- rating with 5 "know-how" stars
- picture
- article
- info about the author
- related articles
- integration of comment plugin TALVEO

Target Market(s)

SEO folks

Industry/Entity Type

Seo

Logo Text

Do-it yourself SEO

Number of Pages Required

2 page

Font styles to use
Sans Serif

Colors

Designer to choose colors to be used in the design.

```html
<!DOCTYPE html>
<html lang="en">
<head>
<meta charset="utf-8">
<title>rankvale – Know-how</title>
<link href="https://fonts.googleapis.com/css2?family=Roboto:wght@400;500;700&display=swap" rel="stylesheet">
<style>
:root{
  --red:#dc3737;
  --red-dark:#b52222;
  --red-ghost:#b62a2a;
  --white:#ffffff;
  --ink:#111111;
  --ink-soft:#4a4f4d;
  --grey:#9a9a9a;
  --doc-grey:#9b9b9b;
  --doc-dark:#434a48;
}
*{box-sizing:border-box;margin:0;padding:0}
html,body{width:1200px;height:675px;overflow:hidden;background:var(--white);font-family:"Roboto",sans-serif}
.page{position:relative;width:1200px;height:675px;overflow:hidden}

/* header */
.site-header{position:absolute;left:0;top:0;width:1200px;height:70px;background:var(--white)}
.social{position:absolute;left:70px;top:24px;display:flex;gap:16px;font-size:14px;font-weight:500;color:var(--ink)}
.brand{position:absolute;left:520px;top:18px;display:flex;align-items:center;gap:8px;font-size:29px;font-weight:500;color:var(--ink);letter-spacing:.5px}
.brand-dot{width:20px;height:20px;border-radius:50%;background:var(--red)}
.top-nav{position:absolute;right:70px;top:23px;display:flex;gap:20px;font-size:17px;color:var(--ink)}

/* search band */
.search-band{position:absolute;left:0;top:70px;width:1200px;height:180px;background:var(--red)}
.search-label{position:absolute;left:134px;top:44px;font-size:15px;font-weight:500;color:var(--white)}
.search-mark{position:absolute;left:72px;top:104px;width:30px;height:30px;border-radius:50%;border:3px solid var(--white)}
.search-input{position:absolute;left:134px;top:98px;font-size:41px;font-weight:700;color:var(--white);line-height:1}
.search-input .ghost{color:var(--red-ghost)}
.caret{display:inline-block;width:2px;height:40px;background:var(--white);vertical-align:-6px;margin:0 -1px}
.search-line{position:absolute;left:134px;top:163px;width:841px;height:2px;background:var(--white)}
.search-btn{position:absolute;left:982px;top:102px;width:148px;height:44px;border-radius:22px;background:var(--white);display:flex;align-items:center;justify-content:center;gap:12px;color:var(--red);font-size:21px;font-weight:500}

/* suggestions */
.suggestions{position:absolute;left:0;top:250px;width:1200px;height:242px;background:var(--white);box-shadow:0 3px 8px rgba(0,0,0,.12);z-index:2;list-style:none}
.suggestion{height:60.5px;display:flex;align-items:center;font-size:13px;font-weight:500;color:var(--ink-soft)}
.suggestion svg{margin-left:78px;margin-right:40px}
.suggestion.active{background:var(--red-dark);color:var(--white)}

/* content below */
.cat-list{position:absolute;left:70px;top:478px;list-style:none;font-size:16px;color:var(--grey)}
.cat-list li{height:29px;display:flex;align-items:center;gap:10px}
.cat-icon{width:14px;height:14px;border-radius:50%;background:var(--red)}
.article-list{position:absolute;top:473px;list-style:none;font-size:15.5px;color:var(--ink)}
.article-list li{height:31.6px;display:flex;align-items:center;gap:14px}
.col-a{left:422px}.col-b{left:834px}
.section-title{position:absolute;top:642px;display:flex;align-items:center;gap:12px;color:var(--red);font-size:21px;font-weight:500}
.popular{left:70px;top:648px}
.content-seo{left:379px}
.technical-seo{left:792px}
</style>
</head>
<body>
<div class="page">
  <header class="site-header">
    <div class="social"><span>chirpnet</span><span>brivella</span></div>
    <div class="brand"><span class="brand-dot"></span>rankvale</div>
    <nav class="top-nav"><span>Blog</span><span>Contact</span></nav>
  </header>

  <section class="search-band">
    <p class="search-label">What are you looking for?</p>
    <span class="search-mark"></span>
    <div class="search-input">Acc<span class="caret"></span><span class="ghost">ount</span></div>
    <div class="search-line"></div>
    <div class="search-btn">
      <svg width="18" height="18" viewBox="0 0 18 18"><circle cx="7.5" cy="7.5" r="6" fill="none" stroke="currentColor" stroke-width="2"/><line x1="12" y1="12" x2="17" y2="17" stroke="currentColor" stroke-width="2" stroke-linecap="round"/></svg>
      Search
    </div>
  </section>

  <ul class="suggestions">
    <li class="suggestion active"><svg width="16" height="19" viewBox="0 0 16 19"><path d="M2 0h8l6 6v11a2 2 0 0 1-2 2H2a2 2 0 0 1-2-2V2a2 2 0 0 1 2-2z" fill="#fff"/></svg>How Do I Close My Account?</li>
    <li class="suggestion"><svg width="16" height="19" viewBox="0 0 16 19"><path d="M2 0h8l6 6v11a2 2 0 0 1-2 2H2a2 2 0 0 1-2-2V2a2 2 0 0 1 2-2z" fill="#434a48"/></svg>Customizing the theme colors</li>
    <li class="suggestion"><svg width="16" height="19" viewBox="0 0 16 19"><path d="M2 0h8l6 6v11a2 2 0 0 1-2 2H2a2 2 0 0 1-2-2V2a2 2 0 0 1 2-2z" fill="#434a48"/></svg>Recommended Plugins</li>
    <li class="suggestion"><svg width="16" height="19" viewBox="0 0 16 19"><path d="M2 0h8l6 6v11a2 2 0 0 1-2 2H2a2 2 0 0 1-2-2V2a2 2 0 0 1 2-2z" fill="#434a48"/></svg>Modifiying The Background Image &amp; Color</li>
  </ul>

  <ul class="cat-list">
    <li><span class="cat-icon"></span>Technical SEO</li>
    <li><span class="cat-icon"></span>Link Building</li>
    <li><span class="cat-icon"></span>Influencer Marketing</li>
    <li><span class="cat-icon"></span>Paid Marketing</li>
    <li><span class="cat-icon"></span>Analytics &amp; Measurement</li>
  </ul>

  <ul class="article-list col-a">
    <li><svg width="16" height="19" viewBox="0 0 16 19"><path d="M2 0h8l6 6v11a2 2 0 0 1-2 2H2a2 2 0 0 1-2-2V2a2 2 0 0 1 2-2z" fill="#9b9b9b"/></svg>How Do I Change My Email?</li>
    <li><svg width="16" height="19" viewBox="0 0 16 19"><path d="M2 0h8l6 6v11a2 2 0 0 1-2 2H2a2 2 0 0 1-2-2V2a2 2 0 0 1 2-2z" fill="#9b9b9b"/></svg>Where Can I Upload My Avatar?</li>
    <li><svg width="16" height="19" viewBox="0 0 16 19"><path d="M2 0h8l6 6v11a2 2 0 0 1-2 2H2a2 2 0 0 1-2-2V2a2 2 0 0 1 2-2z" fill="#9b9b9b"/></svg>How Do I Change My Timezone?</li>
    <li><svg width="16" height="19" viewBox="0 0 16 19"><path d="M2 0h8l6 6v11a2 2 0 0 1-2 2H2a2 2 0 0 1-2-2V2a2 2 0 0 1 2-2z" fill="#9b9b9b"/></svg>How Do I Change My Password?</li>
  </ul>
  <ul class="article-list col-b">
    <li><svg width="16" height="19" viewBox="0 0 16 19"><path d="M2 0h8l6 6v11a2 2 0 0 1-2 2H2a2 2 0 0 1-2-2V2a2 2 0 0 1 2-2z" fill="#9b9b9b"/></svg>How Do I Change My Email?</li>
    <li><svg width="16" height="19" viewBox="0 0 16 19"><path d="M2 0h8l6 6v11a2 2 0 0 1-2 2H2a2 2 0 0 1-2-2V2a2 2 0 0 1 2-2z" fill="#9b9b9b"/></svg>Where Can I Upload My Avatar?</li>
    <li><svg width="16" height="19" viewBox="0 0 16 19"><path d="M2 0h8l6 6v11a2 2 0 0 1-2 2H2a2 2 0 0 1-2-2V2a2 2 0 0 1 2-2z" fill="#9b9b9b"/></svg>How Do I Change My Timezone?</li>
    <li><svg width="16" height="19" viewBox="0 0 16 19"><path d="M2 0h8l6 6v11a2 2 0 0 1-2 2H2a2 2 0 0 1-2-2V2a2 2 0 0 1 2-2z" fill="#9b9b9b"/></svg>How Do I Change My Password?</li>
  </ul>

  <h2 class="section-title popular">Popular Articles</h2>
  <h2 class="section-title content-seo"><svg width="26" height="26" viewBox="0 0 26 26"><rect width="26" height="26" fill="#dc3737"/><rect x="5" y="7" width="16" height="3" fill="#fff"/><rect x="5" y="16" width="16" height="3" fill="#fff"/></svg>Content SEO</h2>
  <h2 class="section-title technical-seo"><svg width="28" height="26" viewBox="0 0 28 26"><path d="M18 2l8 8-14 14a4 4 0 0 1-8-8z" fill="#dc3737"/><circle cx="25" cy="21" r="3" fill="#dc3737"/></svg>Technical SEO</h2>
</div>
</body>
</html>
```